Visitenkarten-Design für ein Juwelier Geschäft
Zielgruppe
Juwelier Geschäft in modernem offenen design.
Zielgruppe sind kunden und partner/marken
Aufgabenstellung
schlichtes edles Design.
karten sollen später geprägt werden und einen goldschnitt erhalten

```html
<!DOCTYPE html>
<html lang="de">
<head>
<meta charset="utf-8">
<title>Juwelier Brandmeyer – Visitenkarte</title>
<link href="https://fonts.googleapis.com/css2?family=Poppins:wght@300;400;600;700&display=swap" rel="stylesheet">
<style>
  :root {
    --backdrop: #e6e7ea;
    --card: #f2f3f5;
    --copper: #b47d58;
    --ink: #3a3b3e;
    --shadow: rgba(40, 35, 30, 0.22);
  }
  * { margin: 0; padding: 0; box-sizing: border-box; }
  html, body {
    width: 1200px; height: 418px; overflow: hidden;
    background: var(--backdrop);
    font-family: "Poppins", sans-serif;
  }
  .stage { position: relative; width: 1200px; height: 418px; }
  .card {
    position: absolute; top: 72px;
    width: 411px; height: 274px;
    background: var(--card);
    box-shadow: 0 3px 10px var(--shadow);
  }
  .card--front { left: 94px; }
  .card--back { left: 694px; }

  .accent-bar {
    position: absolute; left: 2px;
    width: 8px; background: var(--copper);
  }

  .wordmark { position: absolute; left: 22px; color: var(--copper); font-weight: 600; line-height: 1; }
  .wordmark__line1 { display: block; font-size: 18px; letter-spacing: 0.5px; }
  .wordmark__line2 { display: block; font-size: 38px; letter-spacing: 0.5px; margin-top: 4px; }
  .card--front .wordmark { top: 26px; }
  .card--back .wordmark { top: 106px; }
  .card--back .accent-bar { top: 103px; height: 58px; }

  .person { position: absolute; left: 22px; top: 150px; color: var(--copper); line-height: 1; }
  .person__name { font-weight: 300; font-size: 27px; letter-spacing: 0.3px; }
  .person__role { font-weight: 700; font-size: 18px; letter-spacing: 0.5px; margin-top: 4px; }
  .card--front .accent-bar { top: 141px; height: 60px; }

  .contact {
    position: absolute; left: 258px; top: 173px;
    list-style: none; color: var(--ink);
    font-size: 10.5px; line-height: 12.5px;
  }
  .contact__item { display: flex; align-items: flex-start; gap: 8px; margin-bottom: 4px; }
  .contact__icon { width: 13px; height: 13px; flex: none; margin-top: 0; }

  .website {
    position: absolute; right: 23px; bottom: 30px;
    font-size: 11.5px; color: var(--ink);
  }
</style>
</head>
<body>
<main class="stage">
  <section class="card card--front" aria-label="Vorderseite">
    <div class="wordmark">
      <span class="wordmark__line1">JUWELIER</span>
      <span class="wordmark__line2">BRANDMEYER</span>
    </div>
    <div class="accent-bar"></div>
    <div class="person">
      <div class="person__name">JOHN DOE</div>
      <div class="person__role">DIRECTOR</div>
    </div>
    <ul class="contact">
      <li class="contact__item">
        <svg class="contact__icon" viewBox="0 0 24 24" fill="none" stroke="currentColor" stroke-width="1.8"><path d="M12 22s7-7 7-12a7 7 0 0 0-14 0c0 5 7 12 7 12z"/><circle cx="12" cy="10" r="2.6"/></svg>
        <span>Niederlassung Lingen<br>Marktstraße 14<br>49808 Lingen</span>
      </li>
      <li class="contact__item">
        <svg class="contact__icon" viewBox="0 0 24 24" fill="none" stroke="currentColor" stroke-width="1.8"><path d="M5 3h4l2 5-2.5 1.5a11 11 0 0 0 6 6L16 13l5 2v4a2 2 0 0 1-2 2A16 16 0 0 1 3 5a2 2 0 0 1 2-2z"/><path d="M15 3a6 6 0 0 1 6 6M15 7a2 2 0 0 1 2 2"/></svg>
        <span>+49 0591-204417</span>
      </li>
      <li class="contact__item">
        <svg class="contact__icon" viewBox="0 0 24 24" fill="none" stroke="currentColor" stroke-width="1.8"><rect x="3" y="5" width="18" height="14" rx="1"/><path d="M3 6l9 7 9-7"/></svg>
        <span>info@brandmeyer.de</span>
      </li>
    </ul>
  </section>

  <section class="card card--back" aria-label="Rückseite">
    <div class="accent-bar"></div>
    <div class="wordmark">
      <span class="wordmark__line1">JUWELIER</span>
      <span class="wordmark__line2">BRANDMEYER</span>
    </div>
    <div class="website">www.brandmeyer.de</div>
  </section>
</main>
</body>
</html>
```